VELIR Convention 2025 Quebec City

We would like to have a poster for the promotion and publicity of a convention for VELIR. The goal is to obtain in A4 format and in US letter format (8.5 X 11) a poster for the upcoming convention in Quebec City.
Here are the 2 images (Mirla-8 and Mirla-24) that we chose yesterday and that inspire us.

Also the 3 posters of previous Conventions (Cahier T+V 252, 261 & 273) As a model of what we are looking for.

As for what should also appear on the poster of the Quebec Convention 2025, here are the main points:

Mandatory at the very top of the poster: VELIR and the wings (as on the posters of the previous Conventions attached) or at least leave such a space free because I believe that the printers of the High Circle are redoing this acronym by themselves- same for the review Onde-Pâle.
Then the rest can be left to the imagination of the artists.

Here are the important things that should be included:
Talbrin Pact
Quebec city
October 11 and 12, 2025
Light (This is the theme of the convention)
Glow to warm every shore (That's the name of the convention)

Please post it in French and NO RELATION TO RELIGIOUS OR RELIGION!!! :)

The website of the organization for more info if required is: www.onde-pale.example

If you think of anything else to add, no problem.

Target Market(s)

VELIR members only

Industry/Entity Type

OSBL - Organisme philosophique ( non religieux )

Font styles to use
Serif
Sans Serif

Requirements
Must have
• VELIR wings logo
Nice to have
• All in French and without reference to religion, also the GOLD color is appreciated
Should not have
• Of aspect or reference to the religious

```html
<!DOCTYPE html>
<html lang="fr">
<head>
<meta charset="utf-8">
<title>Talbrin Pact 2025 — Lumière</title>
<link rel="stylesheet" href="https://fonts.googleapis.com/css2?family=Cinzel:wght@400;600&family=Great+Vibes&family=Tinos&display=swap">
<style>
  :root {
    --backdrop: #d3c9b3;
    --poster-dark: #1f1611;
    --band-dark: #2a1b12;
    --gold: #e7c46a;
    --gold-light: #f6df9a;
    --gold-deep: #a7741f;
    --cream: #f4ecdc;
    --white: #ffffff;
  }
  * { box-sizing: border-box; margin: 0; padding: 0; }
  html, body {
    width: 1200px; height: 1200px; overflow: hidden;
    background: var(--backdrop);
  }
  .poster {
    position: absolute; left: 246px; top: 106px;
    width: 696px; height: 986px;
    background: var(--poster-dark);
    box-shadow: 0 6px 18px rgba(0,0,0,.25);
    overflow: hidden;
  }
  .brand {
    position: absolute; left: 0; top: 0; width: 100%; height: 104px;
    display: flex; flex-direction: column; align-items: center; justify-content: center;
    color: var(--gold);
    font-family: "Cinzel", serif;
  }
  .brand-name { font-size: 22px; font-weight: 600; letter-spacing: 10px; }
  .brand-order { font-size: 12px; letter-spacing: 1px; margin-top: 10px; }
  .pact-band {
    position: absolute; left: 0; top: 110px; width: 100%; height: 42px;
    background: var(--band-dark);
    border-top: 2px solid #4a3424;
    display: flex; align-items: center; justify-content: center;
    font-family: "Cinzel", serif; font-size: 26px; letter-spacing: 4px;
    color: var(--cream);
  }
  .light-art {
    position: absolute; left: 0; top: 156px; width: 100%; height: 520px;
    background:
      radial-gradient(ellipse 48% 42% at 50% 62%, rgba(214,150,45,.55), rgba(120,75,20,.3) 55%, transparent 100%),
      linear-gradient(180deg, var(--poster-dark) 0%, #2a1a0c 55%, #3a2410 82%, var(--poster-dark) 100%);
  }
  .theme {
    position: absolute; left: 0; top: 218px; width: 100%;
    text-align: center;
    font-family: "Great Vibes", cursive; font-size: 66px; font-weight: 400; color: var(--white);
  }
  .headline {
    position: absolute; left: 0; top: 668px; width: 100%;
    text-align: center;
    font-family: "Tinos", serif; font-weight: 400;
    color: var(--white); line-height: 1;
  }
  .headline-small { display: block; font-size: 40px; }
  .headline-big {
    display: block; font-size: 72px; margin: 8px 0 8px;
    color: var(--gold);
    background: linear-gradient(180deg, var(--gold-light), var(--gold) 50%, var(--gold-deep));
    -webkit-background-clip: text; background-clip: text; -webkit-text-fill-color: transparent;
  }
  .info-band {
    position: absolute; left: 0; bottom: 0; width: 100%; height: 90px;
    background: linear-gradient(90deg, #5a3514 0%, #a06d2c 35%, #e4bd62 70%, #f3d27a 100%);
    border-top: 2px solid var(--gold-light);
    display: flex; align-items: center;
    font-family: "Tinos", serif; color: var(--poster-dark);
  }
  .dates { display: flex; align-items: center; padding-left: 34px; width: 340px; }
  .dates-days { font-size: 52px; color: var(--white); }
  .dates-month { font-size: 20px; line-height: 1.1; margin-left: 12px; color: var(--white); }
  .divider { width: 2px; height: 60px; background: var(--poster-dark); }
  .place { display: flex; align-items: center; padding-left: 18px; font-size: 24px; }
  .place svg { margin-right: 10px; }
</style>
</head>
<body>
  <main class="poster">
    <header class="brand">
      <span class="brand-name">VELIR</span>
      <span class="brand-order">ORDRE DE L'ONDE-PÂLE</span>
    </header>
    <div class="pact-band">TALBRIN PACT</div>
    <div class="light-art" role="img" aria-label="Illustration : anneau de lumière dorée se levant sur un horizon réfléchissant, avec rayons et poussière scintillante"></div>
    <h2 class="theme">Lumière</h2>
    <h1 class="headline">
      <span class="headline-small">RAYONNE POUR</span>
      <span class="headline-big">RÉCHAUFFER</span>
      <span class="headline-small">CHAQUE RIVE</span>
    </h1>
    <footer class="info-band">
      <div class="dates">
        <span class="dates-days">11-12</span>
        <span class="dates-month">OCTOBRE<br>2025</span>
      </div>
      <span class="divider"></span>
      <div class="place">
        <svg width="26" height="26" viewBox="0 0 24 24" aria-hidden="true">
          <circle cx="12" cy="12" r="11" fill="#1f1611"/>
          <path d="M12 5.5a4.2 4.2 0 0 0-4.2 4.2c0 3.1 4.2 7.8 4.2 7.8s4.2-4.7 4.2-7.8A4.2 4.2 0 0 0 12 5.5z" fill="#e4bd62"/>
          <circle cx="12" cy="9.7" r="1.6" fill="#1f1611"/>
        </svg>
        LA VILLE DE QUÉBEC
      </div>
    </footer>
  </main>
</body>
</html>
```